Business Card for my New Brokerage

Looking to get a business card design for my new Real Estate Brokerage.
I want it with Picture, Phone Number, Email, Website, Office Address
Name and Designation. Please add logo too.

Target Market(s)

Real Estate Investors or Home Buyers

Industry/Entity Type

Real Estate

Contact Information for Business Card

Name, Email, Phone Number, website, email, office address

Colors
EB3D1F
EC4F4E
F09395
F8D3D4
FCEDEE

Requirements
Must have
• Minimalistic, Clean, Modern, Photo
Nice to have
• White and Red Colors

```html
<!DOCTYPE html>
<html lang="en">
<head>
<meta charset="utf-8">
<title>Ember Realty Inc — Business Card</title>
<link rel="stylesheet" href="https://fonts.googleapis.com/css2?family=Montserrat:wght@400;700&family=Lato:wght@400&family=Libre+Baskerville&display=swap">
<style>
  :root {
    --red: #e21f26;
    --gold-light: #faf6d2;
    --gold: #ecd77a;
    --gold-deep: #d9b44a;
    --white: #f7f9fb;
    --ink: #3a3a3a;
    --bg: #efe9e4;
    --photo-top: #f1f1f1;
    --photo-suit: #2b2f45;
  }
  * { margin: 0; padding: 0; box-sizing: border-box; }
  html, body { width: 1200px; height: 1097px; overflow: hidden; }
  body {
    background: var(--bg);
    display: flex; flex-direction: column; align-items: center; justify-content: center;
    gap: 70px;
    font-family: "Montserrat", sans-serif;
  }
  .card {
    position: relative; width: 700px; height: 400px; overflow: hidden;
    box-shadow: 0 8px 24px rgba(0,0,0,.18);
  }
  .card--front { background: linear-gradient(115deg, var(--gold-deep) 0%, var(--gold-light) 45%, var(--gold) 80%, var(--gold-deep) 100%); }
  .card--back { background: var(--white); }
  .card__shapes { position: absolute; inset: 0; }

  .brand-name {
    font-family: "Montserrat", sans-serif; font-weight: 700; color: var(--red);
    line-height: 1.1; letter-spacing: .5px;
  }

  .front__content { position: absolute; left: 0; right: 90px; top: 135px; text-align: center; }
  .front__content .brand-name { font-size: 40px; }
  .address { font-family: "Libre Baskerville", serif; font-size: 17px; color: var(--ink); margin-top: 24px; }

  .photo {
    position: absolute; left: 70px; top: 110px; width: 210px; height: 210px;
    border: 2px solid var(--red); padding: 6px;
  }
  .photo__fill { width: 100%; height: 100%; background: linear-gradient(180deg, var(--photo-top) 0%, var(--photo-top) 55%, var(--photo-suit) 100%); }

  .back__content { position: absolute; left: 310px; top: 52px; }
  .back__content .brand-name { font-size: 32px; }
  .person { margin-top: 34px; }
  .person__name { font-size: 24px; font-weight: 700; color: var(--red); }
  .person__name span { font-weight: 400; font-size: 18px; }
  .person__title { font-family: "Lato", sans-serif; font-size: 13px; color: var(--ink); letter-spacing: .5px; margin-top: 2px; }
  .contacts { list-style: none; margin-top: 14px; }
  .contacts li { display: flex; align-items: center; gap: 10px; font-family: "Lato", sans-serif; font-size: 17px; color: var(--ink); margin-bottom: 8px; }
  .contacts svg { width: 18px; height: 18px; flex: none; }
</style>
</head>
<body>

<section class="card card--front" aria-label="Card front">
  <svg class="card__shapes" viewBox="0 0 700 400" aria-hidden="true">
    <polygon points="0,345 575,345 625,90 675,90 620,400 0,400" fill="var(--red)"/>
    <polygon points="655,175 700,110 700,330" fill="var(--gold)"/>
  </svg>
  <div class="front__content">
    <p class="brand-name">Ember Realty Inc</p>
    <p class="address">1280 Alder Creek Dr, Lakeview, CA 90000</p>
  </div>
</section>

<section class="card card--back" aria-label="Card back">
  <svg class="card__shapes" viewBox="0 0 700 400" aria-hidden="true">
    <polygon points="0,345 575,345 625,90 675,90 620,400 0,400" fill="var(--red)"/>
    <polygon points="655,175 700,110 700,330" fill="var(--gold)"/>
  </svg>
  <div class="photo"><div class="photo__fill" role="img" aria-label="Portrait photo of Daniel Reed"></div></div>
  <div class="back__content">
    <p class="brand-name">Ember Realty Inc</p>
    <div class="person">
      <p class="person__name">DANIEL <span>REED</span></p>
      <p class="person__title">CHIEF EXECUTIVE OFFICER</p>
    </div>
    <ul class="contacts">
      <li><svg viewBox="0 0 20 20"><circle cx="10" cy="10" r="10" fill="var(--red)"/><path d="M7 5l2 2-1 1.5c.6 1.4 1.6 2.4 3 3L12.5 10l2 2-1.3 1.5C9.5 13.5 6.5 10.5 6 6.5z" fill="#fff"/></svg>555-210-4478</li>
      <li><svg viewBox="0 0 20 20"><circle cx="10" cy="10" r="10" fill="var(--red)"/><rect x="5" y="6.5" width="10" height="7" fill="#fff"/><path d="M5 6.5l5 4 5-4" stroke="var(--red)" fill="none"/></svg>hello@emberrealty.com</li>
      <li><svg viewBox="0 0 20 20"><circle cx="10" cy="10" r="10" fill="var(--red)"/><g stroke="#fff" fill="none" stroke-width="1.2"><circle cx="10" cy="10" r="5.5"/><ellipse cx="10" cy="10" rx="2.3" ry="5.5"/><path d="M4.5 10h11"/></g></svg>www.emberrealty.com</li>
    </ul>
  </div>
</section>

</body>
</html>
```